Korvell Plant Services

We are a heavy diesel mechanical business with additional air con certificates, remapping engine rebuilt

Contact Information for Business Card

Company Name, Director Name, Managing Director, Contact details, email and website

Font styles to use
Serif
Script

```html
<!DOCTYPE html>
<html lang="en">
<head>
<meta charset="utf-8">
<title>Korvell Plant Services – Business Card</title>
<link rel="stylesheet" href="https://fonts.googleapis.com/css2?family=Arimo:wght@400;700&display=swap">
<style>
  :root {
    --bg: #2e2e2e;
    --card-dark: #1c1c1c;
    --card-light: #ffffff;
    --navy: #14166b;
    --ink: #1a1a1a;
    --silver: #bdbdbd;
    --text: #222222;
  }
  * { box-sizing: border-box; margin: 0; padding: 0; }
  html, body { width: 1200px; height: 875px; overflow: hidden; }
  body {
    background: var(--bg);
    font-family: "Arimo", Arial, sans-serif;
    position: relative;
  }
  .card {
    position: absolute;
    left: 320px;
    width: 560px;
    height: 320px;
    border-radius: 18px;
    overflow: hidden;
  }
  .card--front { top: 100px; background: var(--card-dark); }
  .card--back { top: 455px; background: var(--card-light); }

  .brand {
    position: absolute;
    display: flex;
    align-items: center;
    gap: 14px;
  }
  .brand__dot {
    width: 22px; height: 22px;
    border-radius: 50%;
  }
  .brand__name {
    font-weight: 700;
    line-height: 1.05;
  }
  .card--front .brand { left: 0; right: 0; top: 0; bottom: 0; justify-content: center; }
  .card--front .brand__dot { background: var(--silver); }
  .card--front .brand__name { color: var(--silver); font-size: 38px; }

  .card--back .brand { left: 34px; top: 112px; width: 190px; gap: 10px; }
  .card--back .brand__dot { background: var(--navy); flex: none; width: 16px; height: 16px; }
  .card--back .brand__name { color: var(--navy); font-size: 25px; }

  .divider {
    position: absolute;
    left: 238px; top: 52px;
    width: 2px; height: 180px;
    background: var(--navy);
  }
  .details { position: absolute; left: 258px; top: 44px; right: 20px; }
  .details__name {
    color: var(--navy);
    font-weight: 700;
    font-size: 22px;
    letter-spacing: .5px;
  }
  .details__role { color: var(--text); font-size: 14px; margin-top: 3px; }
  .contact { list-style: none; margin-top: 12px; }
  .contact li {
    display: flex; align-items: flex-start; gap: 9px;
    color: var(--text); font-size: 12.5px; line-height: 1.35;
  }
  .contact li + li { margin-top: 2px; }
  .contact li.gap { margin-top: 10px; }
  .contact svg { flex: none; width: 12px; height: 12px; margin-top: 2px; fill: var(--navy); }
  .contact svg.icon-globe { fill: none; stroke: var(--navy); stroke-width: 1.2; }

  .band-line {
    position: absolute; left: 0; right: 0; bottom: 38px;
    height: 2px; background: var(--ink);
  }
  .band {
    position: absolute; left: 0; right: 0; bottom: 0;
    height: 30px; background: var(--navy);
  }
</style>
</head>
<body>
  <section class="card card--front" aria-label="Card front">
    <div class="brand">
      <span class="brand__dot"></span>
      <span class="brand__name">Korvell Plant Services</span>
    </div>
  </section>

  <section class="card card--back" aria-label="Card back">
    <div class="brand">
      <span class="brand__dot"></span>
      <span class="brand__name">Korvell Plant Services</span>
    </div>
    <div class="divider"></div>
    <div class="details">
      <h1 class="details__name">DANIEL HART</h1>
      <p class="details__role">Managing Director</p>
      <ul class="contact">
        <li>
          <svg viewBox="0 0 12 12"><path d="M6 0a4 4 0 0 0-4 4c0 3 4 8 4 8s4-5 4-8a4 4 0 0 0-4-4zm0 5.5A1.5 1.5 0 1 1 6 2.5a1.5 1.5 0 0 1 0 3z"/></svg>
          <span>72 Quarry Road, Unit 4<br>Hollin Vale, Westshire, HV4 2RD</span>
        </li>
        <li class="gap">
          <svg viewBox="0 0 12 12"><path d="M2.5 0l2 2.5-1.2 1.5c.8 1.8 2.2 3.2 4 4L8.8 6.8 11.3 8.8 10 11.5C5 11 1 7 .5 2z"/></svg>
          <span>(555) 210-4470</span>
        </li>
        <li>
          <svg viewBox="0 0 12 12"><path d="M3 0h6a1 1 0 0 1 1 1v10a1 1 0 0 1-1 1H3a1 1 0 0 1-1-1V1a1 1 0 0 1 1-1zm0 1.5v8h6v-8z"/></svg>
          <span>(555) 210-4471</span>
        </li>
        <li>
          <svg viewBox="0 0 12 12"><path d="M3 0h6v3H3zM1 4h10v5H9v3H3V9H1zm3 4v3h4V8z"/></svg>
          <span>(555) 210-4472</span>
        </li>
        <li>
          <svg viewBox="0 0 12 12"><path d="M0 2h12v1L6 7 0 3zm0 2.5l6 4 6-4V10H0z"/></svg>
          <span>info@korvellplant.com</span>
        </li>
        <li>
          <svg class="icon-globe" viewBox="0 0 12 12"><circle cx="6" cy="6" r="5.2"/><ellipse cx="6" cy="6" rx="2.2" ry="5.2"/><path d="M.8 6h10.4"/></svg>
          <span>korvellplant.com</span>
        </li>
      </ul>
    </div>
    <div class="band-line"></div>
    <div class="band"></div>
  </section>
</body>
</html>
```